Half-off Holiday Sale: Tremorwell Academy

The online course called Tremorwell Academy. Once a year, I run a 1/2 off special (expired Dec 31). You can see what the school is all about here: tremorwell-academy.net and I'll attach a picture of the current ad we're running.
www.tremorwell-academy.net

Please stick with the brain/puzzle logo as the theme, but make the 50% off appealing and inviting.

** I plan on paying for more than one design. I'd like to buy a few different ones!

Target Market(s)

People with Parkinson's disease and their families.

Industry/Entity Type

medical care/ education

Requirements
Must have
• TA School (Tremorwell Academy) logo; Must say "50% off" or something like that.

```html
<!DOCTYPE html>
<html lang="en">
<head>
<meta charset="utf-8">
<title>Tremorwell Academy – Special Offer 50% Off</title>
<link rel="stylesheet" href="https://fonts.googleapis.com/css2?family=Archivo+Black&family=Dancing+Script:wght@700&family=Titillium+Web:wght@700&family=Arimo:wght@400;700&display=swap">
<style>
  :root {
    --teal-deep: #4db6ac;
    --teal-mid: #80cbc4;
    --teal-band: #85ccc7;
    --teal-pale: #b3dfdf;
    --teal-mist: #e0f2f1;
    --rust: #c8603c;
    --white: #ffffff;
    --ink: #333333;
  }
  html, body {
    margin: 0;
    padding: 0;
    width: 1200px;
    height: 1000px;
    overflow: hidden;
    background: var(--white);
  }
  .canvas {
    position: relative;
    width: 1200px;
    height: 1000px;
    background: var(--white);
  }
  .decor {
    position: absolute;
    left: 0;
    top: 0;
  }
  .brand {
    position: absolute;
    left: 500px;
    top: 318px;
    width: 175px;
    text-align: center;
  }
  .brand-dot {
    display: block;
    width: 38px;
    height: 38px;
    margin: 0 auto 6px;
    border-radius: 50%;
    background: var(--teal-deep);
  }
  .brand-name {
    margin: 0;
    font-family: "Titillium Web", sans-serif;
    font-weight: 700;
    font-size: 12.5px;
    line-height: 1;
    color: var(--teal-deep);
    letter-spacing: 0.2px;
    white-space: nowrap;
  }
  .brand-tagline {
    margin: 2px 0 0;
    font-family: "Arimo", sans-serif;
    font-size: 6px;
    color: var(--teal-deep);
    white-space: nowrap;
  }
  .offer-title {
    position: absolute;
    left: 442px;
    top: 430px;
    margin: 0;
    font-family: "Dancing Script", cursive;
    font-weight: 700;
    font-size: 46px;
    line-height: 1;
    color: var(--teal-deep);
    white-space: nowrap;
    transform: rotate(-2deg);
    transform-origin: left bottom;
  }
  .offer-amount {
    position: absolute;
    left: 383px;
    top: 458px;
    margin: 0;
    font-family: "Archivo Black", sans-serif;
    font-size: 170px;
    line-height: 1;
    letter-spacing: -8px;
    color: var(--rust);
    white-space: nowrap;
    transform: scaleX(0.74);
    transform-origin: left top;
  }
  .offer-percent {
    position: absolute;
    left: 574px;
    top: 478px;
    font-family: "Archivo Black", sans-serif;
    font-size: 72px;
    line-height: 1;
    color: var(--teal-deep);
  }
  .offer-off {
    position: absolute;
    left: 568px;
    top: 553px;
    font-family: "Archivo Black", sans-serif;
    font-size: 48px;
    line-height: 1;
    letter-spacing: -3px;
    color: var(--rust);
    white-space: nowrap;
  }
  .deadline {
    position: absolute;
    left: 363px;
    top: 611px;
    width: 300px;
    height: 25px;
    background: var(--rust);
    color: var(--white);
    font-family: "Arimo", sans-serif;
    font-weight: 700;
    font-size: 19px;
    line-height: 25px;
    letter-spacing: 1.4px;
    text-align: right;
    padding-right: 12px;
    box-sizing: border-box;
    white-space: nowrap;
  }
  .visit-band {
    position: absolute;
    left: 363px;
    top: 675px;
    width: 411px;
    height: 51px;
    background: var(--teal-band);
    color: var(--white);
    font-family: "Arimo", sans-serif;
    font-size: 13px;
    line-height: 51px;
    letter-spacing: 1.2px;
    text-align: right;
    padding-right: 26px;
    box-sizing: border-box;
    white-space: nowrap;
  }
  .photo-credit {
    position: absolute;
    left: 683px;
    top: 728px;
    font-family: "Arimo", sans-serif;
    font-size: 5.5px;
    color: var(--ink);
    white-space: nowrap;
  }
</style>
</head>
<body>
<div class="canvas">
  <svg class="decor" width="1200" height="1000" viewBox="0 0 1200 1000">
    <defs>
      <linearGradient id="puzzle-tone" x1="0" y1="0" x2="1" y2="1">
        <stop offset="0" stop-color="#a9c4c3"/>
        <stop offset="0.5" stop-color="#c5d6d3"/>
        <stop offset="1" stop-color="#9db7b5"/>
      </linearGradient>
    </defs>
    <polygon class="corner-triangle" points="363,263 557,263 363,398" fill="var(--teal-pale)"/>
    <line class="stripe-mist" x1="396" y1="388" x2="522" y2="268" stroke="var(--teal-mist)" stroke-width="16" stroke-linecap="round"/>
    <line class="stripe-mid" x1="416" y1="344" x2="492" y2="270" stroke="var(--teal-mid)" stroke-width="20" stroke-linecap="round"/>
    <line class="stripe-deep" x1="505" y1="303" x2="546" y2="265" stroke="var(--teal-deep)" stroke-width="17" stroke-linecap="round"/>
    <path class="puzzle-photo" role="img" aria-label="Photo of scattered jigsaw puzzle pieces, cut in a puzzle-piece shape"
      fill="url(#puzzle-tone)"
      d="M837,300 C812,298 796,318 804,340 C810,355 790,365 760,364 L700,364 C686,400 683,440 690,462 C705,470 740,455 755,480 C768,505 755,525 725,530 C700,535 690,540 686,560 C683,590 688,615 700,632 L770,630 C800,630 810,645 800,665 C790,685 812,700 837,698 Z"/>
  </svg>

  <div class="brand">
    <span class="brand-dot"></span>
    <p class="brand-name">TREMORWELL ACADEMY</p>
    <p class="brand-tagline">An Online Course for Patients and Providers</p>
  </div>

  <h1 class="offer-title">Special Offer</h1>
  <p class="offer-amount">50</p>
  <span class="offer-percent">%</span>
  <span class="offer-off">OFF</span>

  <div class="deadline">until December 31</div>
  <div class="visit-band">visit now www.tremorwell-academy.net</div>
  <div class="photo-credit">https://picvault.net/en/photo/1551311</div>
</div>
</body>
</html>
```